Cleaning & Maintenance Direct mail flyer for marketing to realtors and property managers

2 SIDED FLYER , ONE SIDE IS ALREADY COMPLETE, JUST NEEDS SMALL REVISIONS. I WOULD LIKE TO CREATE 2ND SIDE

Direct mail flyer promoting cleaning and maintenance to realtor. Highlight our services with text and images. I have uploaded a PDF with all of the content and instructions SEE PDF ATTACHED

FRONT SIDE SIDE #1
This side will keep similar format as above:

Revise content as listed below

Top:
Change: Don’t Miss Out We’re Offering to
The Time For Extraordinary Listings Is NOW!

Change: On All Of Our Services To
Transform Your Properties

KEEP: FREE ESTIMATES

Carpet Cleaning
Van Mounted Steam Clean
Dirt Stain & Odor Removal
Revitalize Your Carpets

Window Washing
Interior / Exterior + Solar Panels
Let The Sunshine In!

Flood & Mold Rescue
We Respond In 30 Mins 24/7
We Turn Chaos To Calm

Tile Grout & Stone
Transform Your Floors
Restores The Natural Luster

Power Washing
Remove Dirt, Grime & Mold
Restore Original Charm

Handyman Help
Plumbing, Painting, Drywall & More
Yes, We Will Fix It!

BACKSIDE SIDE # 2 Layout inspiration below

Transform Your Properties
The Time For Extraordinary Listings Is Now!

πŸ”₯ Ignite Your Listings With Birchline Cleaning & Restoration! πŸ”₯

____________________________________________________________________________
I would like the following content to appear as a letter/message written on a sticky note / note paper:
Dear Realtor,

Are You Ready To Dominate The Market? Unlock The Power Of Success

Our All-In-One Services Revolutionize Your Pre-Listing Cleaning And Maintenance Game.
No More Frantic Searching Or Managing Multiple Vendorsβ€”Seize Back Your Valuable Time!

Clean Listings Sell & Rent Faster:
Impress Potential Buyers And Tenants With Immaculate Properties.

Birchline A Brand You Can Count On:
Trust Our Reputation For Exceptional Service And Customer Care.

Don't Miss Out On The Opportunity To Elevate Your Properties To The Next Level.

Call Or Text 555-014-7296 For A Free Estimate
_________________________________________________________________________

The Birchline Guarantee:
βœ… Fast Turnovers
βœ… Reduced Stress
βœ… Streamlined Process
βœ… Cost-Effective Solutions
βœ… Time-Saving Convenience
βœ… Emergency Superheroes
βœ… Lightning-Fast Turnovers
βœ… Trusted And Reliable Service

Transform Your Properties With Clean & Fix Makeovers

Birchline Services:
βœ… Carpet Cleaning
βœ… Window Washing
βœ… Power Washing
βœ… Soft Washing
βœ… Tile & Grout
βœ… Natural stone
βœ… Flood & Mold Rescue
βœ… Handyman
βœ… Trash Hauling

Join The Ranks Of San Diego's Leading Realtors Who Rely On Our Expertise.

Target Market(s)

Realtors & Property Managers

Industry/Entity Type

Cleaning & Maintenance

Font styles to use
Other font styles liked:
• Small Caps Font Type

Colors
0054AA
0677BA
7BADD7
CADEEF
E8F1F8
EB3D1F
EC4F4E
F09395
F8D3D4
FCEDEE

Requirements
Must have
• 2 Sided Flyer. Side #1 is a copy of previous project, we will revise content and improve aesthetics. Side #2 We need to create using the content uploaded on word doc file

```html
<!DOCTYPE html>
<html lang="en">
<head>
<meta charset="utf-8">
<title>Transform Your Properties – Birchline Cleaning &amp; Restoration</title>
<link href="https://fonts.googleapis.com/css2?family=Kaushan+Script&family=Oswald:wght@300;400;500&family=Russo+One&display=swap" rel="stylesheet">
<style>
  :root {
    --navy-deep: #141766;
    --navy: #1d2785;
    --navy-band: #22398c;
    --gold: #f2c500;
    --white: #ffffff;
    --panel: #dedede;
    --heading-blue: #1f3ea0;
    --alert-red: #e8272a;
    --ink: #111111;
    --paper: #f3f3f4;
    --rule: #b9b9c2;
    --tape: #f1d94a;
  }
  * { box-sizing: border-box; margin: 0; padding: 0; }
  html, body { width: 1200px; height: 986px; overflow: hidden; background: var(--navy); }
  .flyer {
    position: relative; width: 1200px; height: 986px; overflow: hidden;
    background: linear-gradient(180deg, var(--navy-deep) 0%, var(--navy) 40%, #202d90 100%);
    font-family: "Oswald", sans-serif; color: var(--white);
  }
  .skyline-photo {
    position: absolute; left: 0; top: 0; width: 1200px; height: 300px;
    background: linear-gradient(180deg, #6f6aa8 0%, #9a7ab0 30%, #b58a8c 55%, #5b4a6e 75%, rgba(29,39,133,0) 100%);
  }
  .title-box {
    position: absolute; left: 54px; top: 26px; width: 372px; height: 184px;
    background: var(--navy-deep); padding: 4px;
  }
  .title-box-inner {
    border: 2px solid var(--white); height: 100%; text-align: center; padding-top: 8px;
  }
  .title-main { font-weight: 500; color: var(--gold); font-size: 78px; line-height: 76px; letter-spacing: -1px; text-shadow: 3px 3px 0 #000; }
  .title-sub { font-weight: 500; color: var(--gold); font-size: 52px; line-height: 50px; letter-spacing: -1px; text-shadow: 3px 3px 0 #000; }
  .title-tagline { font-weight: 400; font-size: 21px; line-height: 30px; margin-top: 4px; }
  .ignite {
    position: absolute; left: 44px; top: 270px; font-weight: 400; font-size: 42px; line-height: 52px; letter-spacing: -0.5px;
  }
  .info-panel {
    position: absolute; background: var(--panel); border: 8px solid var(--white); border-radius: 40px;
  }
  .guarantee { left: 34px; top: 389px; width: 528px; height: 203px; padding: 16px 0 0 28px; }
  .services { left: 42px; top: 657px; width: 526px; height: 239px; padding: 20px 0 0 26px; }
  .panel-heading { font-family: "Russo One", sans-serif; color: var(--heading-blue); font-size: 25px; line-height: 30px; }
  .bullet-columns { display: flex; margin-top: 8px; }
  .bullet-list { list-style: none; }
  .bullet-list li { color: var(--ink); font-size: 22px; line-height: 32.5px; font-weight: 300; position: relative; padding-left: 20px; white-space: nowrap; }
  .bullet-list li::before { content: ""; position: absolute; left: 2px; top: 14px; width: 7px; height: 7px; border-radius: 50%; background: var(--heading-blue); }
  .guarantee .bullet-list:first-child { width: 217px; }
  .services .bullet-columns { margin-top: 14px; }
  .services .bullet-list:first-child { width: 247px; }
  .makeovers {
    position: absolute; left: 42px; top: 608px; color: var(--alert-red); font-size: 25px; line-height: 40px; font-weight: 400; white-space: nowrap;
  }
  .worker-illustration {
    position: absolute; left: 552px; top: 514px; width: 186px; height: 394px;
    background: linear-gradient(180deg, #2a1e8f 0%, #1a1a6a 60%, #111 100%); border-radius: 60px 60px 20px 20px;
  }
  .note {
    position: absolute; left: 588px; top: 91px; width: 580px; height: 770px;
    background-color: var(--paper);
    background-image: repeating-linear-gradient(180deg, transparent 0 30px, var(--rule) 30px 31px);
    background-position: 0 12px;
    transform: rotate(-5.4deg); transform-origin: top left;
    border-radius: 0 0 0 26px; box-shadow: 2px 4px 10px rgba(0,0,0,0.25);
    font-family: "Kaushan Script", cursive; color: var(--ink); font-size: 19px; line-height: 31px;
    padding: 62px 20px 0 52px;
  }
  .note p { margin-bottom: 31px; white-space: nowrap; }
  .note .indented { padding-left: 56px; margin-bottom: 37px; }
  .note .call { color: var(--alert-red); font-size: 21px; padding-left: 70px; }
  .tape {
    position: absolute; left: 988px; top: 10px; width: 192px; height: 42px; background: var(--tape);
    transform: rotate(11deg);
  }
  .bottom-band {
    position: absolute; left: 0; top: 906px; width: 1200px; height: 80px; background: var(--navy-band);
    text-align: center; font-size: 37px; line-height: 80px; font-weight: 400; white-space: nowrap; letter-spacing: -0.3px;
  }
</style>
</head>
<body>
<main class="flyer">
  <div class="skyline-photo" role="img" aria-label="Photograph of the San Diego waterfront skyline at dusk"></div>

  <header class="title-box">
    <div class="title-box-inner">
      <h1 class="title-main">TRANSFORM</h1>
      <div class="title-sub">YOUR PROPERTIES</div>
      <p class="title-tagline">The Time For Extraordinary Listings Is Now!</p>
    </div>
  </header>

  <h2 class="ignite">Ignite Your Listings With<br>Birchline Cleaning &amp; Restoration!</h2>

  <section class="info-panel guarantee">
    <h3 class="panel-heading">The Birchline Guarantee:</h3>
    <div class="bullet-columns">
      <ul class="bullet-list">
        <li>Fast Turnovers</li>
        <li>Reduced Stress</li>
        <li>Streamlined Process</li>
        <li>Cost-Effective Solutions</li>
      </ul>
      <ul class="bullet-list">
        <li>Time-Saving Convenience</li>
        <li>Emergency Superheroes</li>
        <li>Lightning-Fast Turnovers</li>
        <li>Trusted And Reliable Service</li>
      </ul>
    </div>
  </section>

  <p class="makeovers">Transform Your Properties With Clean &amp; Fix Makeovers</p>

  <section class="info-panel services">
    <h3 class="panel-heading">Birchline Services:</h3>
    <div class="bullet-columns">
      <ul class="bullet-list">
        <li>Carpet Cleaning</li>
        <li>Window Washing</li>
        <li>Power Washing</li>
        <li>Soft Washing</li>
        <li>Tile &amp; Grout</li>
      </ul>
      <ul class="bullet-list">
        <li>Natural stone</li>
        <li>Flood &amp; Mold Rescue</li>
        <li>Handyman</li>
        <li>Trash Hauling</li>
      </ul>
    </div>
  </section>

  <div class="worker-illustration" role="img" aria-label="Illustration of a uniformed cleaner in a blue cap and shirt pushing a floor mop"></div>

  <article class="note">
    <p>Dear Realtor,</p>
    <p>Are you ready to dominate the market? Unlock the<br>power of success</p>
    <p>Our all-in-one services revolutionize your pre-listing<br>cleaning and maintenance game.<br>No more frantic searching or managing multiple<br>vendors—seize back your valuable time!</p>
    <p class="indented">Clean listings sell &amp; rent faster:<br>impress potential buyers and tenants<br>with immaculate properties.</p>
    <p class="indented">Birchline a brand you can count on:<br>trust our reputation for exceptional service and<br>customer care.</p>
    <p class="indented">Don't miss out on the opportunity to elevate your<br>properties to the next level.</p>
    <p class="call">Call or text 555-014-7296 for a free estimate</p>
  </article>
  <div class="tape"></div>

  <footer class="bottom-band">JOIN THE RANKS OF SAN DIEGO'S LEADING REALTORS WHO RELY ON OUR EXPERTISE.</footer>
</main>
</body>
</html>
```